Commercial Business Card - stand out, clean, simple, unique.

commercial real estate group located in Texas. Called Verrowmere Real Estate. We want a unique yet clean and professional card. On one side I would like the VM to be by itself or to look as unique or tasteful as possible. We have the logo in white, black, and color in case a black background or something similar looks best on one side. We need a space for our name, email, cell. website. And possibly room for a phrase or city.

Contact Information for Business Card

Name, Title, Email, Phone Number, website

```html
<!DOCTYPE html>
<html lang="en">
<head>
<meta charset="utf-8">
<title>Verrowmere Real Estate – Business Card</title>
<link href="https://fonts.googleapis.com/css2?family=Cinzel:wght@600&family=Open+Sans:wght@400;600&display=swap" rel="stylesheet">
<style>
  :root {
    --stage: #e8e5df;
    --card-light: #f1f1ef;
    --card-dark: #5b5b5c;
    --navy: #1f2a63;
    --royal: #34489a;
    --copper: #d0683a;
  }
  * { box-sizing: border-box; margin: 0; padding: 0; }
  html, body {
    width: 1200px; height: 1200px; overflow: hidden;
    background: var(--stage);
  }
  .canvas { position: relative; width: 1200px; height: 1200px; }
  .card {
    position: absolute; left: 120px; width: 960px; height: 548px;
    box-shadow: 0 6px 18px rgba(0,0,0,0.18);
  }
  .card--back { top: 40px; background: var(--card-dark); }
  .card--front { top: 612px; background: var(--card-light); }

  .wordmark {
    display: flex; align-items: center; gap: 18px;
    font-family: "Cinzel", serif; font-weight: 600;
    letter-spacing: 0.04em; white-space: nowrap;
  }
  .wordmark__square { width: 30px; height: 30px; flex: none; }

  .card--back .wordmark {
    position: absolute; left: 50%; top: 50%;
    transform: translate(-50%, -50%);
    font-size: 46px; color: var(--royal);
  }
  .card--back .wordmark__square { background: var(--royal); width: 38px; height: 38px; }

  .card--front .wordmark {
    position: absolute; left: 60px; top: 60px;
    font-size: 38px; color: var(--navy);
  }
  .card--front .wordmark__square { background: var(--navy); }

  .contact {
    position: absolute; left: 520px; top: 300px;
    font-family: "Open Sans", sans-serif; color: var(--navy);
  }
  .contact__name { font-size: 34px; font-weight: 600; line-height: 1.05; }
  .contact__title { font-size: 22px; color: var(--copper); letter-spacing: 0.04em; }
  .contact__rule { width: 160px; height: 5px; background: var(--navy); margin: 4px 0 18px; }
  .contact__list { list-style: none; }
  .contact__item {
    display: flex; align-items: center; gap: 40px;
    font-size: 22px; line-height: 1.6; letter-spacing: 0.02em;
  }
  .contact__icon { width: 22px; height: 22px; flex: none; color: var(--copper); }
</style>
</head>
<body>
<div class="canvas">

  <section class="card card--back" aria-label="Card back">
    <div class="wordmark"><span class="wordmark__square"></span>Verrowmere Real Estate</div>
  </section>

  <section class="card card--front" aria-label="Card front">
    <div class="wordmark"><span class="wordmark__square"></span>Verrowmere Real Estate</div>

    <div class="contact">
      <p class="contact__name">Mara Delgado</p>
      <p class="contact__title">CEO / Founder</p>
      <div class="contact__rule"></div>
      <ul class="contact__list">
        <li class="contact__item">
          <svg class="contact__icon" viewBox="0 0 24 24" fill="none" stroke="currentColor" stroke-width="2" stroke-linecap="round" stroke-linejoin="round"><path d="M22 16.9v3a2 2 0 0 1-2.2 2 19.8 19.8 0 0 1-8.6-3.1 19.5 19.5 0 0 1-6-6A19.8 19.8 0 0 1 2.1 4.2 2 2 0 0 1 4.1 2h3a2 2 0 0 1 2 1.7c.1 1 .4 1.9.7 2.8a2 2 0 0 1-.5 2.1L8 9.9a16 16 0 0 0 6 6l1.3-1.3a2 2 0 0 1 2.1-.4c.9.3 1.8.6 2.8.7a2 2 0 0 1 1.8 2z"/></svg>
          +111 - 2222 - 333
        </li>
        <li class="contact__item">
          <svg class="contact__icon" viewBox="0 0 24 24" fill="none" stroke="currentColor" stroke-width="2" stroke-linejoin="round"><rect x="2" y="5" width="20" height="14"/><path d="M2 5l10 8 10-8"/></svg>
          yourmail@mail.com
        </li>
        <li class="contact__item">
          <svg class="contact__icon" viewBox="0 0 24 24" fill="none" stroke="currentColor" stroke-width="2"><circle cx="12" cy="12" r="10"/><path d="M2 12h20M12 2c3 3 3 17 0 20M12 2c-3 3-3 17 0 20"/></svg>
          www.yourwebsite.com
        </li>
      </ul>
    </div>
  </section>

</div>
</body>
</html>
```